Ondas Tierra - Stationery and Presentation Materials
Biz card, letterhead, envelope, presentation folder
Bright & Fun-filled
Martin Coble
E.S.
Tel. +503.2417.8836
Cel. +503.7396.1052
U.S. +1.800.555.0147 x3061
U.S.
ondastierra.led@correoplano.com
PLEASE, DON'T POST EMAIL IN DRAFTS.
--The business is rental of large LED screens for visuals, which are made of thousands of tiny lights.
---Please give a range of crazy/abstract as well as aggressive but traditional/corporate concepts for all items in subtitle.
---The presentation folder is to digitally insert fotos later for printing. Borders are key. A CD will be included, on a plastic peg anywhere in the folder, and CD design must blend with folder graphics on the point where CD sits.
Minimal.
---try wrap-around logo
----1 "wild concept" if anyone is willing - background is very tiny, SHINING, white lights (almost pixel-looking), with the logo symbol on top.

```html
<!DOCTYPE html>
<html lang="es">
<head>
<meta charset="utf-8">
<title>Ondas Tierra – Tarjeta de presentación</title>
<link href="https://fonts.googleapis.com/css2?family=Nunito:wght@400;700;800&display=swap" rel="stylesheet">
<style>
  :root {
    --stage: #ece9e4;
    --card-white: #ffffff;
    --orange-light: #f9a12a;
    --orange-deep: #ef5a22;
    --brand-red: #ec4a24;
    --wave-blue: #1f4fa3;
    --wave-blue-light: #3d7fd0;
    --text-white: #ffffff;
  }
  * { margin: 0; padding: 0; box-sizing: border-box; }
  html, body {
    width: 1200px;
    height: 965px;
    overflow: hidden;
    background: var(--stage);
    font-family: "Nunito", Arial, sans-serif;
  }
  .business-card {
    position: absolute;
    left: 150px;
    top: 224px;
    width: 900px;
    height: 517px;
    border-radius: 26px;
    overflow: hidden;
    background: var(--card-white);
    box-shadow: 0 10px 30px rgba(0,0,0,0.18);
  }
  .card-band {
    position: absolute;
    inset: 0;
    width: 100%;
    height: 100%;
  }
  .brand-name {
    position: absolute;
    left: 0;
    right: 0;
    top: 95px;
    text-align: center;
    font-weight: 800;
    font-size: 100px;
    letter-spacing: -1px;
    color: var(--brand-red);
    line-height: 1;
  }
  .holder-name {
    position: absolute;
    right: 498px;
    top: 372px;
    font-weight: 700;
    font-size: 36px;
    line-height: 1.2;
    color: var(--text-white);
    white-space: nowrap;
  }
  .contact-divider {
    position: absolute;
    left: 426px;
    top: 348px;
    width: 2px;
    height: 140px;
    background: var(--text-white);
  }
  .contact-list {
    position: absolute;
    left: 444px;
    top: 346px;
    list-style: none;
    color: var(--text-white);
    font-size: 21px;
    line-height: 28px;
    white-space: nowrap;
  }
  .contact-list b { font-weight: 800; }
</style>
</head>
<body>
  <article class="business-card">
    <svg class="card-band" viewBox="0 0 900 517" preserveAspectRatio="none" aria-hidden="true">
      <defs>
        <linearGradient id="bandOrange" x1="0" y1="0" x2="1" y2="0">
          <stop offset="0" stop-color="#ef5a22"/>
          <stop offset="0.45" stop-color="#f9a12a"/>
          <stop offset="1" stop-color="#ef5a22"/>
        </linearGradient>
        <linearGradient id="waveBlue" x1="0" y1="0" x2="1" y2="0">
          <stop offset="0" stop-color="#1f4fa3"/>
          <stop offset="0.6" stop-color="#3d7fd0"/>
          <stop offset="1" stop-color="#1f4fa3"/>
        </linearGradient>
      </defs>
      <path d="M0 268 C 180 320, 420 330, 600 300 C 720 282, 820 270, 900 272 L900 290 C 800 286, 700 300, 600 312 C 420 336, 200 336, 0 300 Z" fill="url(#waveBlue)"/>
      <path d="M0 318 C 200 350, 420 338, 600 312 C 720 295, 820 286, 900 290 L900 517 L0 517 Z" fill="url(#bandOrange)"/>
    </svg>

    <p class="brand-name">ondastierra</p>

    <h1 class="holder-name">Martin Coble</h1>
    <span class="contact-divider"></span>
    <ul class="contact-list">
      <li>E.S.</li>
      <li><b>Tel :</b> +503.2417.8836</li>
      <li><b>Cell :</b> +503.7396.1052</li>
      <li><b>U.S :</b> +1.800.555.0147 x3061</li>
      <li><b>Email :</b> yourmail@correoplano.com</li>
    </ul>
  </article>
</body>
</html>
```